New company cut sheet “one page” description of services (double sided) *

Harrowgate Ridge Partners, LLC is looking for a newly designed one page sheet that describes the companies services. We will provide our logo and some images and content.

Target Market(s)

Companies that need to raise money or real estate owners that are looking to finance or re-finance. Raising debt and equity financing for companies looking to raise 2MM to 100MM

Industry/Entity Type

Real Estate Development

Font styles to use
Serif
Decorative

Colors

Designer to choose colors to be used in the design.

Requirements
Must have
• Logo, website, company description, why we are better. We would like some possible graphics that are regal and classy. Please list that our offices are located on Linden Row in New York, Philadelphia, Houston and Austin
Nice to have
• Good graphics that gives the impression we are very high class and professional. Maybe a skyline or office buildings. Classy and elegant. High end business class. We are raising money for indivual projects and companies from 2MM to 100MM

```html
<!DOCTYPE html>
<html lang="en">
<head>
<meta charset="utf-8">
<title>Harrowgate Ridge Partners — Cut Sheet</title>
<link rel="stylesheet" href="https://fonts.googleapis.com/css2?family=Libre+Bodoni:wght@700&family=Fira+Sans:ital,wght@0,300;0,400;0,500;1,400&display=swap">
<style>
  :root {
    --stage: #e9e9ee;
    --paper: #ffffff;
    --ink-navy: #1b1f73;
    --night: #0c0e2c;
    --violet: #5c62ad;
    --violet-soft: #7f85c9;
    --band: #1c1d86;
    --white: #ffffff;
    --serif: "Libre Bodoni", "Bodoni Moda", Georgia, serif;
    --sans: "Fira Sans", Arial, sans-serif;
  }
  * { box-sizing: border-box; margin: 0; padding: 0; }
  html, body { width: 1200px; height: 1000px; overflow: hidden; }
  body { background: var(--stage); position: relative; font-family: var(--sans); }

  .sheet { position: absolute; left: 300px; width: 600px; height: 465px; overflow: hidden; }
  .sheet--front { top: 21px; }
  .sheet--back { top: 507px; display: flex; }

  /* Front */
  .cover-image {
    position: absolute; inset: 0;
    background:
      radial-gradient(ellipse 70% 45% at 60% 20%, var(--violet) 0%, rgba(92,98,173,0.55) 45%, rgba(12,14,44,0) 80%),
      radial-gradient(ellipse 60% 40% at 10% 10%, rgba(127,133,201,0.7), rgba(12,14,44,0) 70%),
      linear-gradient(180deg, #23275a 0%, var(--night) 70%);
  }
  .cover-title {
    position: absolute; left: 20px; bottom: 32px;
    display: flex; align-items: center; color: var(--white);
  }
  .cover-title__name { font-family: var(--serif); font-weight: 700; font-size: 18px; letter-spacing: 0.2px; }
  .cover-title__rule { width: 1px; height: 18px; background: var(--white); margin: 0 12px; opacity: 0.8; }
  .cover-title__motto { font-family: var(--sans); font-weight: 300; font-size: 13px; }

  /* Back — left column */
  .services { width: 300px; height: 100%; background: var(--paper); padding: 30px 23px 0; position: relative; color: var(--ink-navy); }
  .services__title { font-family: var(--serif); font-weight: 700; font-size: 16px; line-height: 22px; }
  .services__intro { font-size: 10.5px; line-height: 13px; margin-top: 12px; }
  .services__rule { width: 68px; height: 3px; background: var(--ink-navy); margin-top: 14px; }
  .services__subtitle { font-weight: 400; font-size: 13px; margin-top: 30px; }
  .reasons { list-style: none; margin-top: 16px; }
  .reasons li { position: relative; padding-left: 16px; font-size: 7.6px; line-height: 10px; margin-bottom: 10px; padding-right: 8px; }
  .reasons li::before { content: ""; position: absolute; left: 0; top: 2px; width: 6px; height: 6px; background: var(--ink-navy); }
  .services__values { position: absolute; left: 23px; bottom: 12px; font-size: 6.5px; letter-spacing: 1.4px; }

  /* Back — right column */
  .brand-panel { width: 300px; height: 100%; position: relative; color: var(--white); }
  .brand-image {
    position: absolute; left: 0; top: 0; width: 300px; height: 361px;
    background:
      radial-gradient(ellipse 60% 50% at 80% 15%, var(--violet-soft), rgba(92,98,173,0) 75%),
      radial-gradient(ellipse 70% 60% at 20% 60%, var(--violet), rgba(92,98,173,0) 80%),
      linear-gradient(160deg, #3a3f8a 0%, #22266a 100%);
  }
  .brand-mark { position: absolute; left: 0; right: 0; top: 195px; text-align: center; }
  .brand-mark__name { font-family: var(--serif); font-weight: 700; font-size: 12px; letter-spacing: 0.3px; }
  .brand-mark__square { display: block; width: 22px; height: 22px; background: var(--white); margin: 0 auto 10px; }
  .brand-mark__motto { font-family: var(--sans); font-style: italic; font-size: 7.5px; margin-top: 3px; }

  .contact-band { position: absolute; left: 0; top: 361px; width: 300px; height: 104px; background: var(--band); padding: 12px 19px 0; font-size: 6.5px; line-height: 8px; }
  .contact-band__heading { font-weight: 500; margin-bottom: 8px; }
  .contact-grid { display: grid; grid-template-columns: 115px 1fr; row-gap: 7px; }
  .contact-grid dt { opacity: 0.85; }
  .contact-band__cities { position: absolute; left: 19px; bottom: 12px; font-size: 6.5px; letter-spacing: 1.4px; }
</style>
</head>
<body>
  <section class="sheet sheet--front">
    <div class="cover-image" role="img" aria-label="Photograph of sweeping blue woven architectural lattice"></div>
    <div class="cover-title">
      <span class="cover-title__name">HARROWGATE RIDGE PARTNERS, LLC</span>
      <span class="cover-title__rule"></span>
      <span class="cover-title__motto">Loyalty. Excellence. Results.</span>
    </div>
  </section>

  <section class="sheet sheet--back">
    <div class="services">
      <h1 class="services__title">Unconventional<br>Capital</h1>
      <p class="services__intro">Over 25 years commercial banking experience in real estate. With access to nontraditional and traditional capital sources alike, Harrowgate Ridge Partners would be honored to earn your business.</p>
      <div class="services__rule"></div>
      <h2 class="services__subtitle">Why Harrowgate Ridge Partners?</h2>
      <ul class="reasons">
        <li>As experienced former commercial bankers, we understand where and how to source the very best financial arrangements for our clients.</li>
        <li>Our vast network of correspondent lenders.</li>
        <li>We have regional &amp; national experience and reach.</li>
        <li>More viable options than traditional sources of capital.</li>
        <li>We understand the importance of privacy and data security so we have created a proprietary system to ensure your data is protected.</li>
        <li>We leverage technology to make the process even more secure and efficient.</li>
        <li>Our process is streamlined in order to serve clients quickly and get project moving forward.</li>
      </ul>
      <p class="services__values">ETHICS | EXCELLENCE| COMMITMENT</p>
    </div>

    <div class="brand-panel">
      <div class="brand-image" role="img" aria-label="Photograph of blue woven architectural lattice curving upward"></div>
      <div class="brand-mark">
        <span class="brand-mark__square"></span>
        <p class="brand-mark__name">HARROWGATE RIDGE PARTNERS</p>
        <p class="brand-mark__motto">Loyalty | Excellence | Results</p>
      </div>
      <div class="contact-band">
        <p class="contact-band__heading">Contact Us</p>
        <dl class="contact-grid">
          <div><dt>Email:</dt><dd>mhale@harrowgateridge.com</dd></div>
          <div><dt>Address:</dt><dd>300 Linden Row, 12th Floor<br>New York, NY 10022</dd></div>
          <div><dt>Phone:</dt><dd>(555) 210-4830</dd></div>
          <div><dt>&nbsp;</dt><dd>www.harrowgateridge.com</dd></div>
        </dl>
        <p class="contact-band__cities">NEW YORK | PHILADELPHIA | HOUSTON | AUSTIN</p>
      </div>
    </div>
  </section>
</body>
</html>
```